Flyer for Merchant Capital Cash Advance business

Need Flyer Design to be advertised on Social Media Platforms and also Print it to Publish it in Magazines.
Flyer Will be printed in different sizes for different publications.
Size 1) 6.25 inches * 11 inches.
Size 2) 8 inch * 11 inch
Size 3) 8 inch * 5.5 I inch
Size 4) 5 inch * 7 inch.
Google “Merchant Capital Cash advance flyer pics” to get an idea.

Flyer Design for Merchant Cash advance business.

Merchant Cash Advance is alternate to bank loans and does not require Personal Guarantee or Collateral.

Target Market(s)

Business owners seeking loan.

Industry/Entity Type

Business Service

Font styles to use
Serif
Sans Serif
Decorative
Script

Colors

Designer to choose colors to be used in the design.

Requirements
Must have
• Content from the Files Uploaded.
• Sharp Colors.
Nice to have
• Would like to see flyer in shape of a Bank Check or a $100 Bill.
• Would like to show a Comparison between Bank Loan and MCA.
• Open to any other ideas.

```html
<!DOCTYPE html>
<html lang="en">
<head>
<meta charset="utf-8">
<title>Business Capital Cash Advance Flyer</title>
<link rel="stylesheet" href="https://fonts.googleapis.com/css2?family=Lato:wght@300;400;700;900&display=swap">
<style>
  :root {
    --blue: #0596ea;
    --blue-light: #64bdf5;
    --navy: #2a4fa0;
    --ink: #444444;
    --ink-dark: #333333;
    --body: #666666;
    --panel: #f4f4f4;
    --faint: #e3e3e3;
    --white: #ffffff;
  }
  * { margin: 0; padding: 0; box-sizing: border-box; }
  html, body { width: 873px; height: 1200px; overflow: hidden; background: var(--white); }
  body { font-family: 'Lato', sans-serif; color: var(--ink); }
  .flyer { position: relative; width: 873px; height: 1200px; overflow: hidden; background: var(--white); }
  .abs { position: absolute; line-height: 1; white-space: nowrap; }

  .logo { left: 114px; top: 108px; font-size: 29px; font-weight: 700; color: var(--ink); letter-spacing: 0.5px; }
  .hero-photo { position: absolute; left: 0; top: 0; }

  .tagline-band { position: absolute; left: 0; top: 213px; width: 873px; height: 72px; background: var(--blue);
    color: var(--white); font-size: 26px; display: flex; align-items: center; justify-content: center; letter-spacing: 0.4px; }
  .headline-band { position: absolute; left: 0; top: 285px; width: 873px; height: 88px; background: var(--panel);
    border-bottom: 3px solid var(--blue); display: flex; align-items: center; justify-content: center;
    font-size: 28px; color: var(--navy); letter-spacing: 0.5px; }
  .headline-band .light { font-weight: 300; margin-right: 9px; }
  .headline-band strong { font-weight: 900; }

  .use-word { font-size: 21px; color: var(--faint); letter-spacing: 0.5px; }
  .use-word.vertical-up { transform: rotate(-90deg); transform-origin: left top; }
  .use-word.vertical-down { transform: rotate(90deg); transform-origin: left top; }

  .benefit { display: flex; align-items: center; font-size: 22px; font-weight: 700; color: var(--ink); letter-spacing: 0.4px; }
  .benefit .tick { width: 25px; height: 25px; margin-right: 14px; flex: none; }
  .benefit-wrap { font-size: 22px; font-weight: 700; color: var(--ink); letter-spacing: 0.4px; }

  .offer-panel { position: absolute; left: 0; top: 0; }

  .offer-title { font-size: 23px; font-weight: 400; color: var(--ink); letter-spacing: 1px; }
  .offer-rule { position: absolute; height: 3px; width: 51px; background: var(--blue); }

  .point { position: absolute; width: 330px; }
  .point-head { display: flex; align-items: center; font-size: 14px; font-weight: 700; color: var(--ink-dark); letter-spacing: 0.6px; }
  .point-head .tick { width: 18px; height: 18px; margin-right: 8px; flex: none; }
  .point-body { margin: 9px 0 0 26px; font-size: 11.6px; line-height: 18px; color: var(--body); letter-spacing: 0.4px; }

  .contact-label { left: 79px; top: 1074px; font-size: 19px; font-weight: 700; color: var(--ink); letter-spacing: 0.6px; opacity: 0.92; }
  .contact-item { display: flex; align-items: center; font-size: 18px; color: var(--ink); letter-spacing: 0.8px; }
  .contact-item svg { margin-right: 9px; flex: none; }
  .divider { position: absolute; left: 519px; top: 1076px; width: 1px; height: 61px; background: var(--navy); }
  .company { right: 85px; top: 1094px; font-size: 22px; font-weight: 700; color: var(--ink); letter-spacing: 1px; }
</style>
</head>
<body>
<main class="flyer">
  <svg class="hero-photo" width="873" height="215" viewBox="0 0 873 215" role="img" aria-label="Photo of business people reviewing loan paperwork at a desk">
    <defs>
      <linearGradient id="heroTone" x1="0" y1="0" x2="1" y2="0.4">
        <stop offset="0" stop-color="#8fb0cc"/>
        <stop offset="0.45" stop-color="#5b7fa6"/>
        <stop offset="1" stop-color="#1f3d66"/>
      </linearGradient>
    </defs>
    <polygon points="428,41 873,41 873,211 380,211" fill="url(#heroTone)"/>
  </svg>
  <div class="abs logo">LOGO HERE</div>

  <div class="tagline-band">Need Business Capital? A convenient alternative to bank loan</div>
  <div class="headline-band"><span class="light">GET</span><strong>BUSINESS CAPITAL CASH ADVANCE</strong></div>

  <div class="abs use-word" style="left:69px;top:404px">Equipment</div>
  <div class="abs use-word" style="left:261px;top:404px">Renovation</div>
  <div class="abs use-word" style="left:458px;top:404px">Advertising</div>
  <div class="abs use-word" style="left:664px;top:404px">Expansion</div>
  <div class="abs use-word vertical-up" style="left:40px;top:583px">Marketing</div>
  <div class="abs use-word vertical-down" style="left:824px;top:484px">Repairs</div>
  <div class="abs use-word" style="left:71px;top:630px">Cashflow</div>
  <div class="abs use-word" style="left:263px;top:630px">Inventory</div>
  <div class="abs use-word" style="left:457px;top:630px">Equipment</div>
  <div class="abs use-word" style="left:663px;top:628px">Improvements</div>

  <svg width="0" height="0" style="position:absolute">
    <defs>
      <symbol id="tickBadge" viewBox="0 0 24 24">
        <circle cx="12" cy="12" r="12" fill="#0596ea"/>
        <path d="M6.8 12.4l3.4 3.4 7-7.2" fill="none" stroke="#fff" stroke-width="2.4" stroke-linecap="round" stroke-linejoin="round"/>
      </symbol>
    </defs>
  </svg>

  <div class="abs benefit" style="left:85px;top:455px"><svg class="tick"><use href="#tickBadge"/></svg>No personal guarantee</div>
  <div class="abs benefit" style="left:85px;top:516px"><svg class="tick"><use href="#tickBadge"/></svg>Bankruptcy - ok</div>
  <div class="abs benefit" style="left:85px;top:580px"><svg class="tick"><use href="#tickBadge"/></svg>Simple one page application</div>
  <div class="abs benefit" style="left:465px;top:455px"><svg class="tick"><use href="#tickBadge"/></svg>No minimum credit score</div>
  <div class="abs benefit" style="left:465px;top:516px"><svg class="tick"><use href="#tickBadge"/></svg>No collateral or guarantors</div>
  <div class="abs benefit-wrap" style="left:503px;top:553px">needed</div>

  <svg class="offer-panel" width="873" height="1020" viewBox="0 0 873 1020" aria-hidden="true">
    <path d="M0,745 Q0,678 95,678 L873,678 L873,942 Q873,1012 790,1012 L0,1012 Z" fill="#f4f4f4"/>
    <path d="M0,1012 L790,1012 Q873,1012 873,942" fill="none" stroke="#64bdf5" stroke-width="8"/>
  </svg>

  <div class="abs offer-title" style="left:77px;top:721px">MERCHANT CASH ADVANCE</div>
  <div class="offer-rule" style="left:332px;top:755px"></div>
  <div class="abs offer-title" style="right:80px;top:721px">SMALL BUSINESS LOANS</div>
  <div class="offer-rule" style="left:741px;top:755px"></div>

  <div class="point" style="left:79px;top:786px">
    <div class="point-head"><svg class="tick"><use href="#tickBadge"/></svg>Lorem ipsum dolor sit amet, consectetur</div>
    <p class="point-body">Lorem ipsum dolor sit amet, consectetur adipiscing elit. Maecenas suscipit, ipsum et lobortis aliquam, lectus dolor convallis urna, sed sodales nisi libero</p>
  </div>
  <div class="point" style="left:79px;top:888px">
    <div class="point-head"><svg class="tick"><use href="#tickBadge"/></svg>Lorem ipsum dolor sit amet, consectetur</div>
    <p class="point-body">Lorem ipsum dolor sit amet, consectetur adipiscing elit. Maecenas suscipit, ipsum et lobortis aliquam, lectus dolor convallis urna, sed sodales nisi libero</p>
  </div>
  <div class="point" style="left:496px;top:784px">
    <div class="point-head"><svg class="tick"><use href="#tickBadge"/></svg>Lorem ipsum dolor sit amet, consectetur</div>
    <p class="point-body">Lorem ipsum dolor sit amet, consectetur adipiscing elit. Maecenas suscipit, ipsum et lobortis aliquam, lectus dolor convallis urna, sed sodales nisi libero</p>
  </div>
  <div class="point" style="left:496px;top:886px">
    <div class="point-head"><svg class="tick"><use href="#tickBadge"/></svg>Lorem ipsum dolor sit amet, consectetur</div>
    <p class="point-body">Lorem ipsum dolor sit amet, consectetur adipiscing elit. Maecenas suscipit, ipsum et lobortis aliquam, lectus dolor convallis urna, sed sodales nisi libero</p>
  </div>

  <div class="abs contact-label">FOR MORE INFO, CONTACT:</div>
  <div class="abs contact-item" style="left:83px;top:1116px">
    <svg width="20" height="15" viewBox="0 0 20 15" aria-hidden="true"><rect x="0" y="0" width="20" height="15" fill="#0596ea"/><path d="M1 1l9 7 9-7M1 14l6.5-6M19 14l-6.5-6" fill="none" stroke="#fff" stroke-width="1.4"/></svg>
    email@email.com
  </div>
  <div class="abs contact-item" style="left:292px;top:1112px">
    <svg width="17" height="18" viewBox="0 0 24 24" aria-hidden="true"><path d="M6.6 10.8a15.1 15.1 0 0 0 6.6 6.6l2.2-2.2a1 1 0 0 1 1-.25 11.4 11.4 0 0 0 3.6.57 1 1 0 0 1 1 1V20a1 1 0 0 1-1 1A17 17 0 0 1 3 4a1 1 0 0 1 1-1h3.5a1 1 0 0 1 1 1c0 1.25.2 2.45.57 3.57a1 1 0 0 1-.25 1z" fill="#0596ea"/></svg>
    +1234578904
  </div>
  <div class="divider"></div>
  <div class="abs company">COMPANY NAME</div>
</main>
</body>
</html>
```